Kestrel Glow Lounge Hair Salon needs a Webpage design

Kestrel Glow Lounge in Englewood is looking to start their web page, url and business emails, we want to be able to upload pictures and videos on the website. we do blow outs , makeup, color, lash extension, gel manicures

Target Market(s)

everyone

Industry/Entity Type

Beauty Salon

Coding

Coded - Design and coding required

Number of Pages Required

5+ page

Font styles to use
Serif

Colors
ffcf3e
9d9d9d
000000
ffffff

Requirements
Must have
• about us, contact us, products, menu, location, gallery, press
Nice to have
• play video gallery

```html
<!DOCTYPE html>
<html lang="en">
<head>
<meta charset="utf-8">
<title>Kestrel Glow Lounge Hair Salon</title>
<link rel="stylesheet" href="https://fonts.googleapis.com/css2?family=Raleway:wght@300;400;700;800&family=Open+Sans:wght@400;700&display=swap">
<style>
  :root {
    --gold: #ffcf3e;
    --grey: #9d9d9d;
    --ink: #000000;
    --paper: #ffffff;
    --heading: #3b3b3b;
    --hero-dark: #1c1419;
    --hero-brown: #4a3826;
    --hero-bronze: #7a6040;
  }
  * { margin: 0; padding: 0; box-sizing: border-box; }
  html, body {
    width: 1200px;
    height: 1000px;
    overflow: hidden;
    background: var(--paper);
  }
  .page {
    position: relative;
    width: 1200px;
    height: 1000px;
    overflow: hidden;
    font-family: "Open Sans", sans-serif;
  }
  .download-note {
    position: absolute;
    left: 79px;
    top: 98px;
    font-family: "Open Sans", sans-serif;
    font-size: 24px;
    letter-spacing: -0.5px;
    color: var(--ink);
  }
  .hero {
    position: absolute;
    left: 0;
    top: 172px;
    width: 1200px;
    height: 588px;
    overflow: hidden;
  }
  .hero-photo {
    position: absolute;
    inset: 0;
    background:
      radial-gradient(ellipse 380px 300px at 230px 200px, rgba(95,72,50,0.85), transparent 70%),
      radial-gradient(ellipse 420px 320px at 1000px 420px, rgba(122,96,64,0.7), transparent 70%),
      radial-gradient(ellipse 300px 260px at 760px 330px, rgba(70,50,48,0.8), transparent 70%),
      linear-gradient(120deg, var(--hero-brown) 0%, var(--hero-dark) 45%, var(--hero-brown) 75%, var(--hero-bronze) 100%);
  }
  .call-us {
    position: absolute;
    left: 68px;
    top: 57px;
    display: flex;
    align-items: center;
    gap: 6px;
    font-family: "Open Sans", sans-serif;
    font-weight: 700;
    font-size: 15px;
    color: var(--paper);
  }
  .call-us .number { color: var(--gold); }
  .main-nav {
    position: absolute;
    left: 329px;
    top: 54px;
    display: flex;
    gap: 9px;
    font-family: "Raleway", sans-serif;
    font-size: 13px;
    font-weight: 400;
    letter-spacing: -0.3px;
    color: var(--paper);
  }
  .main-nav .active { color: var(--gold); }
  .brand-name {
    position: absolute;
    left: 0;
    width: 1200px;
    top: 230px;
    text-align: center;
    font-family: "Raleway", sans-serif;
    font-weight: 300;
    font-size: 64px;
    color: var(--gold);
  }
  .tagline {
    position: absolute;
    left: 0;
    width: 1200px;
    top: 393px;
    text-align: center;
    font-family: "Raleway", sans-serif;
    font-weight: 400;
    font-size: 28px;
    color: var(--paper);
  }
  .scroll-cue {
    position: absolute;
    left: 578px;
    top: 460px;
  }
  .gallery-photo {
    position: absolute;
    background: linear-gradient(160deg, #3a2f2a 0%, #1e1816 60%, #4a3a30 100%);
  }
  .gallery-photo.hair { left: 86px; top: 821px; width: 200px; height: 190px; }
  .gallery-photo.portrait {
    left: 302px; top: 857px; width: 200px; height: 160px;
    background: linear-gradient(180deg, #3f3b38 0%, #2a2624 100%);
  }
  .welcome {
    position: absolute;
    left: 612px;
    top: 848px;
    width: 560px;
    font-family: "Raleway", sans-serif;
    color: var(--heading);
  }
  .welcome h1 {
    font-weight: 800;
    font-size: 35px;
    line-height: 42px;
  }
  .welcome h2 {
    margin-top: 7px;
    font-weight: 700;
    font-size: 19px;
    line-height: 24px;
  }
  .welcome h3 {
    margin-top: 14px;
    font-weight: 300;
    font-size: 26px;
    line-height: 32px;
    letter-spacing: 0.3px;
  }
  .welcome p {
    margin-top: 21px;
    font-family: "Open Sans", sans-serif;
    font-size: 11px;
    color: var(--grey);
    white-space: nowrap;
  }
</style>
</head>
<body>
<div class="page">
  <p class="download-note">PLEASE DOWNLOAD FINAL FILES FROM THIS LINK</p>

  <header class="hero">
    <div class="hero-photo" role="img" aria-label="Photograph of a woman with long flowing brown hair lying among golden dried flowers"></div>

    <div class="call-us">
      <svg width="11" height="11" viewBox="0 0 24 24" aria-hidden="true">
        <path fill="#ffcf3e" d="M6.6 10.8c1.4 2.8 3.8 5.1 6.6 6.6l2.2-2.2c.3-.3.7-.4 1-.2 1.1.4 2.300.6 3.6.6.6 0 1 .4 1 1V20c0 .6-.4 1-1 1C10.6 21 3 13.4 3 4c0-.6.4-1 1-1h3.5c.6 0 1 .4 1 1 0 1.3.2 2.5.6 3.6.1.3 0 .7-.2 1L6.6 10.8z"/>
      </svg>
      <span>Call Us : <span class="number">2015550147</span></span>
    </div>

    <nav class="main-nav">
      <span class="active">HOME</span>
      <span>ABOUT</span>
      <span>PRICE LIST</span>
      <span>PRODUCTS</span>
      <span>LOCATIONS</span>
      <span>PRESS</span>
      <span>BOOK NOW / CONTACT</span>
      <span>SOCIAL</span>
    </nav>

    <div class="brand-name">Kestrel Glow Lounge</div>
    <div class="tagline">Full Service BEAUTY BAR</div>

    <svg class="scroll-cue" width="44" height="28" viewBox="0 0 44 28" aria-hidden="true">
      <polyline points="2,3 22,24 42,3" fill="none" stroke="#ffffff" stroke-width="2.5"/>
    </svg>
  </header>

  <div class="gallery-photo hair" role="img" aria-label="Photograph of glossy dark wavy hair"></div>
  <div class="gallery-photo portrait" role="img" aria-label="Photograph of a woman with long dark hair"></div>

  <section class="welcome">
    <h1>WELCOME TO</h1>
    <h2>KESTREL GLOW LOUNGE IN BRACKEN FALLS VT.</h2>
    <h3>OPEN 7 DAYS A WEEK</h3>
    <p>Kestrel Glow Lounge is a Full service salon offering services ranging from Blowouts</p>
  </section>
</div>
</body>
</html>
```